A new website for Electrical Contractor Business

We are looking for a unique and new WordPress website design which would include 5 Pages - Home Page, Meet the Team, Our Services, Our Projects and Contact Us page.

The global theme for the website needs to be professional but simple to navigate as we cater for both business and home owner customers.

Our core business service is targeted around lighting from single room decorative to large office so the theme should incorporate this in some way.

The home page should include;
Our business logo, Contact number, Email address, small Image rotation box - Highlighting pervious projectsText box - With welcome message, twitter feed news reel/Customer feed back box.

I would also like to see a 2 boxes for the separate customer types we services. Business and Home Owner. each box will have a small image with a small text description with a link to the area of the services page relevant to that customer type.

Meet the team page -This will be introducing potential customers to the team so I would like it to include for each team member. Something like a small image and text area which will introduce an outline of the team members skills and abilities.

Our Services page This page will be outlining the different services on offer to the both customer types business and homeowner. Each service should have an image with text description of the service would good here.

Our projects page-Will include images of pervious projects and work we have completed along with a text area for the project description/ outliner.

Contact Us page - Should include a contact form which should include an option for the customer to quest us to call them back, also a selection box for them to inform us our how they found our details would be good.

Colour - The theme colours can be taken from the logo or feel free to impress with your own imagination.

Remember we are looking for a website that will interest our customers enough to except our services or be drawn further into the website.. So call to action links to other areas of the site/ contact page are welcome

Target Market(s)

Business - Office, warehousing and Large Store - lighting and Power
Home owner lighting and power

Coding

Coded - Design and coding required

Number of Pages Required

5+ page

Font styles to use
Serif
Sans Serif

Colors

Designer to choose colors to be used in the design.

Requirements
Must have
• Logo integrated into the website design - i.e. website colours which allow the logo to blend into the design.
Nice to have
• Custom but professional theme catering to business customers, but also show that we do provide services to home owners too.
Should not have
• Sorry am not interested in one oversized block image on rotation covering half the home page.. Images will be needed but not a single block over sized frame with not text, shape. Please use your imagination when considering this design

```html
<!DOCTYPE html>
<html lang="en">
<head>
<meta charset="utf-8">
<title>Brightline Electrical – Home</title>
<link href="https://fonts.googleapis.com/css2?family=Montserrat:wght@400;500;600;700&display=swap" rel="stylesheet">
<style>
:root{
  --navy:#1e2f6b;
  --blue:#1d46a0;
  --orange:#f26b21;
  --ink:#1b1b1b;
  --text:#333;
  --muted:#8a8a8a;
  --white:#fff;
  --hero-dark:#17171d;
}
*{box-sizing:border-box;margin:0;padding:0}
html,body{width:1200px;height:4317px;overflow:hidden}
body{font-family:'Montserrat',sans-serif;color:var(--text);background:var(--white)}
.wrap{width:984px;margin:0 auto;position:relative;height:100%}
section,header,footer{position:relative;width:1200px;overflow:hidden}
.btn{display:inline-block;border-radius:20px;font-size:10px;font-weight:600;padding:10px 26px;letter-spacing:.3px}
.btn-orange{background:var(--orange);color:var(--white)}
.btn-ghost{border:1.5px solid var(--white);color:var(--white)}
.btn-navy{background:var(--navy);color:var(--white)}
.photo{position:absolute}

/* hero */
.hero{height:740px;background:var(--hero-dark)}
.hero .photo{inset:0;background:linear-gradient(100deg,#1a1d2a 0%,#2a2630 45%,#3a2a22 62%,#6a5a22 78%,#2e2a22 100%)}
.hero .shade{position:absolute;inset:0;background:linear-gradient(90deg,rgba(0,0,0,.45),rgba(0,0,0,0) 70%)}
.brand{position:absolute;left:108px;top:42px;display:flex;flex-direction:column;align-items:center;width:280px}
.brand-mark{width:110px;height:110px;border-radius:50%;border:5px solid var(--white)}
.brand-name{margin-top:18px;font-size:30px;font-weight:500;color:var(--white);letter-spacing:2px;text-align:center;line-height:1.1}
.nav{position:absolute;right:108px;top:46px;display:flex;align-items:center;gap:28px;font-size:12px;font-weight:500;color:var(--white)}
.nav .active{color:var(--orange)}
.nav .search{width:12px;height:12px}
.nav .btn{font-size:11px;padding:12px 22px}
.hero-copy{position:absolute;left:108px;top:362px;color:var(--white)}
.hero-copy h1{font-size:36px;font-weight:600;line-height:1.25;letter-spacing:.5px}
.hero-copy p{font-size:12px;line-height:1.6;margin:10px 0 24px;width:380px}
.hero-copy .btn{margin-right:18px}
.slide-arrow{position:absolute;top:366px;width:28px;height:28px;background:rgba(0,0,0,.5);display:flex;align-items:center;justify-content:center}
.slide-arrow.prev{left:18px}.slide-arrow.next{right:18px}

/* about */
.about{height:580px}
.about .deco{position:absolute;left:-10px;top:360px;width:300px;height:300px;border-radius:50%;border:22px solid rgba(30,47,107,.06)}
.about-copy{position:absolute;left:108px;top:118px;width:470px}
.eyebrow{font-size:22px;font-weight:500;color:var(--ink)}
.about-copy h2{font-size:28px;font-weight:600;color:var(--ink);margin-bottom:24px}
.about-copy p{font-size:11.5px;line-height:2;color:#444;margin-bottom:18px}
.about .backdrop{position:absolute;left:800px;top:82px;width:292px;height:424px;background:var(--navy)}
.about .photo{left:722px;top:40px;width:290px;height:420px;background:linear-gradient(180deg,#b9cbe0,#8ea8c6 50%,#c0704a 78%,#505a70)}

/* service rows */
.row{height:340px}
.row .photo{top:0;width:600px;height:340px}
.row-business .photo{left:0;background:linear-gradient(120deg,#3c4640,#7d8a70 45%,#c4a844 60%,#3e4b42)}
.row-home .photo{right:0;background:linear-gradient(140deg,#e9eaee,#d6dae2 45%,#2f66c8 60%,#dcdfe5)}
.row-copy{position:absolute;top:80px;width:290px}
.row-business .row-copy{left:705px}
.row-home .row-copy{left:108px;top:76px}
.row-copy h3{font-size:16px;font-weight:600;color:var(--ink);margin-bottom:18px}
.row-copy p{font-size:11.5px;line-height:1.95;color:#333;margin-bottom:24px}

/* projects */
.projects{height:370px}
.section-title{font-size:26px;font-weight:500;color:var(--ink);text-align:center}
.projects .section-title{padding-top:48px}
.project-grid{display:flex;gap:26px;margin-top:28px}
.project{width:226px;text-align:center}
.project .thumb{height:208px}
.project span{display:block;font-size:11.5px;font-weight:500;color:var(--navy);margin-top:14px}

/* feedback */
.feedback{height:480px;background:var(--blue)}
.feedback .deco{position:absolute;right:-40px;top:-60px;width:320px;height:320px;border-radius:50%;border:24px solid rgba(255,255,255,.07)}
.feedback .section-title{color:var(--white);padding-top:62px}
.quote-grid{display:flex;gap:18px;margin-top:34px}
.quote{width:485px;height:218px;background:var(--white);padding:26px 30px;position:relative}
.quote .who{display:flex;align-items:center;gap:14px}
.quote .avatar{width:44px;height:44px;border-radius:50%;background:#f0d6c8}
.quote .name{font-size:13px;font-weight:500;color:var(--ink)}
.quote .place{font-size:10.5px;color:var(--orange);margin-top:2px}
.quote .ago{position:absolute;right:30px;top:30px;font-size:10px;color:var(--muted)}
.quote .mark{position:absolute;right:30px;top:56px;font-size:60px;color:#e6e6e6;font-family:Georgia,serif;line-height:1}
.quote p{font-size:11.5px;line-height:2;color:#555;text-align:center;margin-top:30px}
.dots{display:flex;justify-content:center;gap:6px;margin-top:38px}
.dots i{width:7px;height:7px;border-radius:50%;border:1px solid #fff}
.dots i.on{background:var(--orange);border-color:var(--orange)}

/* cta */
.cta{height:400px;background:#3a3430}
.cta .photo{inset:0;background:linear-gradient(100deg,#4a4540,#6a5e52 40%,#7a6a4c 65%,#3a3530)}
.cta .shade{position:absolute;inset:0;background:rgba(20,20,30,.45)}
.cta-copy{position:absolute;inset:0;text-align:center;padding-top:128px;color:var(--white)}
.cta-copy h2{font-size:28px;font-weight:600;line-height:1.7}
.cta-copy .btn{margin-top:24px}

/* news */
.news{height:530px}
.news .section-title{padding-top:78px}
.news-grid{display:flex;gap:42px;margin-top:32px}
.post{width:300px}
.post .thumb{height:198px}
.post time{display:block;font-size:10.5px;color:#444;margin:20px 0 14px}
.post:nth-child(2) time{color:var(--muted)}
.post p{font-size:11.5px;line-height:1.9;color:#222}

/* newsletter */
.newsletter{height:145px;background:var(--orange);color:var(--white)}
.newsletter .wrap{display:flex;align-items:center;justify-content:space-between;padding:0 12px}
.newsletter h3{font-size:22px;font-weight:500;letter-spacing:.5px}
.newsletter p{font-size:11px;margin-top:6px}
.subscribe{width:556px;height:40px;background:var(--white);border-radius:20px;display:flex;justify-content:space-between;align-items:center;padding-left:18px}
.subscribe span{font-size:10px;color:#bbb}
.subscribe .btn{height:40px;padding:14px 36px;font-size:10px}

/* footer */
.footer{height:392px}
.footer .deco{position:absolute;right:-10px;top:130px;width:330px;height:330px;border-radius:50%;border:26px solid rgba(30,47,107,.12)}
.footer-cols{display:flex;padding:60px 0 0 18px}
.col-brand{width:240px;text-align:center}
.col-brand .brand-mark{width:78px;height:78px;border:4px solid var(--navy);margin:0 auto}
.col-brand .brand-name{color:var(--navy);font-size:20px;letter-spacing:1.5px;margin-top:12px}
.col-brand p{text-align:left;font-size:11px;line-height:2;color:#222;margin-top:14px}
.col{width:245px;padding-left:44px}
.col h4{font-size:12px;font-weight:500;color:var(--ink)}
.col h4::after{content:"";display:block;width:26px;height:2px;background:var(--orange);margin:14px 0 30px}
.col li{list-style:none;font-size:11px;color:#222;margin-bottom:18px;display:flex;gap:10px;align-items:flex-start;line-height:1.6}
.col li svg{flex:none;margin-top:3px}
.social{display:flex;gap:16px;font-size:10px;font-weight:500;color:var(--ink)}
.copyright{position:absolute;left:0;right:0;bottom:0;height:54px;border-top:1px solid #e8e8e8;text-align:center;font-size:10.5px;line-height:54px;color:#222}
</style>
</head>
<body>

<header class="hero">
  <div class="photo" role="img" aria-label="Photo of a night-time industrial city skyline with an electrician in a hi-vis vest holding a yellow hard hat"></div>
  <div class="shade"></div>
  <div class="brand">
    <div class="brand-mark"></div>
    <div class="brand-name">BRIGHTLINE ELECTRICAL</div>
  </div>
  <nav class="nav">
    <span class="active">Home</span><span>Our Team</span><span>Services</span><span>Projects</span><span>Contact</span>
    <svg class="search" viewBox="0 0 12 12"><circle cx="5" cy="5" r="4" fill="none" stroke="#fff" stroke-width="1.3"/><line x1="8" y1="8" x2="11.5" y2="11.5" stroke="#fff" stroke-width="1.3"/></svg>
    <span class="btn btn-orange">Get a Free Quote</span>
  </nav>
  <div class="slide-arrow prev"><svg width="8" height="10" viewBox="0 0 8 10"><path d="M6 1 2 5l4 4" fill="none" stroke="#fff" stroke-width="1.5"/></svg></div>
  <div class="slide-arrow next"><svg width="8" height="10" viewBox="0 0 8 10"><path d="M2 1l4 4-4 4" fill="none" stroke="#fff" stroke-width="1.5"/></svg></div>
  <div class="hero-copy">
    <h1>WE PROVIDE LIGHTENING<br>TO YOUR HOUSE AND OFFICES</h1>
    <p>Lorem ipsum dolor sit amet, consectetur adipisicing elit, sed do eiusmod tempor incididunt ut</p>
    <span class="btn btn-orange">READ MORE</span><span class="btn btn-ghost">CONTACT US</span>
  </div>
</header>

<section class="about">
  <div class="deco"></div>
  <div class="about-copy">
    <div class="eyebrow">Welcome</div>
    <h2>About Us</h2>
    <p>Lorem ipsum dolor sit amet, consectetur adipisicing elit, sed do eiusmod tempor incididunt ut labore et dolore magna aliqua. Ut enim ad minim veniam, quis nostrud exercitation ullamco laboris nisi ut aliquip ex ea commodo consequat.</p>
    <p>Duis aute irure dolor in reprehenderit in voluptate velit esse cillum dolore eu fugiat nulla pariatur. Excepteur sint occaecat cupidatat non proident, sunt in culpa qui officia deserunt mollit anim id est laborum. Sed ut perspiciatis unde omnis iste natus error sit voluptatem accusantium doloremque.</p>
  </div>
  <div class="backdrop"></div>
  <div class="photo" role="img" aria-label="Photo of two engineers in hard hats and hi-vis vests looking up at a power pylon"></div>
</section>

<section class="row row-business">
  <div class="photo" role="img" aria-label="Photo of an electrician in a hard hat working among industrial pipes and ducts"></div>
  <div class="row-copy">
    <h3>BUSINESS</h3>
    <p>Lorem ipsum dolor sit amet, consectetur adipisicing elit, sed do eiusmod tempor incididunt ut &nbsp;labore et dolore magna aliqua.</p>
    <span class="btn btn-navy">View Services</span>
  </div>
</section>

<section class="row row-home">
  <div class="row-copy">
    <h3>HOME OWNER</h3>
    <p>Lorem ipsum dolor sit amet, consectetur adipisicing elit, sed do eiusmod tempor incididunt ut &nbsp;labore et dolore magna aliqua.</p>
    <span class="btn btn-navy">View Services</span>
  </div>
  <div class="photo" role="img" aria-label="Photo of an electrician in a blue hard hat fitting a ceiling light"></div>
</section>

<section class="projects">
  <div class="wrap">
    <h2 class="section-title">Latest Projects</h2>
    <div class="project-grid">
      <div class="project"><div class="thumb" role="img" aria-label="Photo of a renovated living room with a grey sofa" style="background:linear-gradient(180deg,#e6e6e6,#c9c9c9 60%,#a9a6a2)"></div><span>Home Renovation</span></div>
      <div class="project"><div class="thumb" role="img" aria-label="Photo of a bright open-plan office" style="background:linear-gradient(180deg,#e8e5df,#d2c8b8 60%,#b8a58a)"></div><span>Office Lightening</span></div>
      <div class="project"><div class="thumb" role="img" aria-label="Photo of an office with rows of ceiling lights and desks" style="background:linear-gradient(180deg,#3a3f48,#cfd4d8 50%,#8ea07a)"></div><span>Lightening and Power</span></div>
      <div class="project"><div class="thumb" role="img" aria-label="Photo of a modern house lit up at dusk" style="background:linear-gradient(180deg,#1f3a7a,#3a5aa0 45%,#e8e4d8 60%,#3c6a2c)"></div><span>Complete Wiring</span></div>
    </div>
  </div>
</section>

<section class="feedback">
  <div class="deco"></div>
  <div class="wrap">
    <h2 class="section-title">Customer Feedback</h2>
    <div class="quote-grid">
      <div class="quote">
        <div class="who"><div class="avatar"></div><div><div class="name">Maya Holden</div><div class="place">California</div></div></div>
        <span class="ago">1 year ago</span><span class="mark">&rdquo;</span>
        <p>Lorem ipsum dolor sit amet, consectetur adipisicing elit, sed do eiusmod tempor incididunt ut labore et dolore magna aliqua. Ut enim ad minim veniam, quis nostrud.</p>
      </div>
      <div class="quote">
        <div class="who"><div class="avatar"></div><div><div class="name">Clara Westby</div><div class="place">Newyork</div></div></div>
        <span class="ago">1 year ago</span><span class="mark">&rdquo;</span>
        <p>Lorem ipsum dolor sit amet, consectetur adipisicing elit, sed do eiusmod tempor incididunt ut labore et dolore magna aliqua. Ut enim ad minim.</p>
      </div>
    </div>
    <div class="dots"><i class="on"></i><i></i><i></i></div>
  </div>
</section>

<section class="cta">
  <div class="photo" role="img" aria-label="Photo of an electrician with a tool belt working in a warehouse corridor"></div>
  <div class="shade"></div>
  <div class="cta-copy">
    <h2>A Wide Tange of Lighting Maintenance for<br>Office, Warehousing and Large Store</h2>
    <span class="btn btn-orange">Contact Us Now</span>
  </div>
</section>

<section class="news">
  <div class="wrap">
    <h2 class="section-title">Latest News</h2>
    <div class="news-grid">
      <article class="post"><div class="thumb" role="img" aria-label="Photo of an engineer in a white hard hat in front of a power pylon" style="background:linear-gradient(160deg,#c9d2dc,#9aa8b8 50%,#3a5a8a)"></div><time>January 11, 2019</time><p>Lorem ipsum dolor sit amet, consectetur adipisicing elit, sed do eiusmod.</p></article>
      <article class="post"><div class="thumb" role="img" aria-label="Photo of an electrician in an orange vest installing cables" style="background:linear-gradient(160deg,#e4e2df,#bdb6ae 50%,#d06a3a)"></div><time>February 21, 2019</time><p>Lorem ipsum dolor sit amet, consectetur adipisicing elit, sed do eiusmod.</p></article>
      <article class="post"><div class="thumb" role="img" aria-label="Photo of a team meeting around a table in a bright office" style="background:linear-gradient(160deg,#eae6e0,#c8bcae 50%,#5a7aa0)"></div><time>March 16, 2019</time><p>Lorem ipsum dolor sit amet, consectetur adipisicing elit, sed do eiusmod.</p></article>
    </div>
  </div>
</section>

<section class="newsletter">
  <div class="wrap">
    <div><h3>Newsletter Subscribe</h3><p>Sign up today for latest product news.</p></div>
    <div class="subscribe"><span>Email</span><span class="btn btn-navy">SUBSCRIBE</span></div>
  </div>
</section>

<footer class="footer">
  <div class="deco"></div>
  <div class="wrap">
    <div class="footer-cols">
      <div class="col-brand">
        <div class="brand-mark"></div>
        <div class="brand-name">BRIGHTLINE ELECTRICAL</div>
        <p>Lorem ipsum dolor sit amet, consectetur adipisicing elit, sed do eiusmod tempor incididunt ut labore et dolore magna aliqua.</p>
      </div>
      <div class="col">
        <h4>Important Links</h4>
        <ul>
          <li>&rsaquo;&nbsp; Home</li><li>&rsaquo;&nbsp; Our Team</li><li>&rsaquo;&nbsp; Services</li><li>&rsaquo;&nbsp; Projects</li><li>&rsaquo;&nbsp; Contact</li>
        </ul>
      </div>
      <div class="col">
        <h4>Connect</h4>
        <ul>
          <li><svg width="9" height="12" viewBox="0 0 9 12"><path d="M4.5 0A4.5 4.5 0 0 0 0 4.5C0 8 4.5 12 4.5 12S9 8 9 4.5A4.5 4.5 0 0 0 4.5 0zm0 6.3a1.8 1.8 0 1 1 0-3.6 1.8 1.8 0 0 1 0 3.6z" fill="#1b1b1b"/></svg>1234 street address,<br>Country</li>
          <li><svg width="11" height="8" viewBox="0 0 11 8"><rect width="11" height="8" fill="#1b1b1b"/><path d="M0 0l5.5 4.5L11 0" fill="none" stroke="#fff"/></svg>hello@brightline-electrical.example</li>
          <li><svg width="10" height="10" viewBox="0 0 10 10"><path d="M2 0l2 2.5-1.2 1.3a6 6 0 0 0 3.4 3.4L7.5 6 10 8l-1.5 2C4 10 0 6 0 1.5z" fill="#1b1b1b"/></svg>123-456-7890</li>
        </ul>
      </div>
      <div class="col">
        <h4>Follow Us</h4>
        <div class="social"><span>Fb</span><span>Tw</span><span>Pn</span><span>Ig</span></div>
      </div>
    </div>
  </div>
  <div class="copyright">© 2019 Brightline Electrical</div>
</footer>

</body>
</html>
```